Emergency Vehicle Installer and Security Firm Needs a Business Card

Our company "Corvalt" need a business card for our Emergency Vehicle Equipment Installation and Infrastructure Security Business. We are contract designers, manufacturers and installers for Emergency Vehicle Fleets. This includes installation of Emergency Lights, Sirens, Vehicle Graphics and Radio Communications. We also supply this products to an international market. We also do consultant, and installation of high level security access, alarm and surveillance equipment for medium to large size businesses.

The design should represent a level of trust in our professionalism and expertise. It should visually display our ongoing relationship with the emergency services, but not overtake our commitment to high level security options.

Target Market(s)

Emergency Services and Businesses requiring high level security

Industry/Entity Type

Business

Contact Information for Business Card

*note complete details will be given to the winning designer for revising. The name "Mark Pell will be used to fill in name".

Mark Pell
Managing Director
Corvalt NZ Limited
Phone: +64 027 604 91352
Email: mark.pell@corvalt-example.co.nz

Requirements
Must have
• Card must be in black. Using our logo on the top as supplied. Designers should try having the reverse side as a blurred image of police lights (red and blue) with our logo in greyscale in the centre (this is not particularly a requirement, but feel free to play around with this option).
Nice to have
• A card design that looks good when spot UV printed. A clean compact and graphic design. A grey scale feel on the front (excluding logo, but you can play around with that idea). Rounded smooth text.
Should not have
• Will update this section as designs come through - feel free to submit what you feel would look good.

```html
<!DOCTYPE html>
<html lang="en">
<head>
<meta charset="utf-8">
<title>Corvalt Business Card</title>
<link rel="stylesheet" href="https://fonts.googleapis.com/css2?family=Open+Sans:wght@400;600;700;800&display=swap">
<style>
  :root {
    --backdrop: #c6c6c5;
    --card-black-light: #1b1b1b;
    --card-black-dark: #070707;
    --card-red-light: #ef4131;
    --card-red-dark: #ee2528;
    --accent-red: #ee2a2a;
    --ink-white: #ffffff;
    --tagline: #ffd3cf;
  }
  * { margin: 0; padding: 0; box-sizing: border-box; }
  html, body {
    width: 1200px;
    height: 900px;
    overflow: hidden;
    background: var(--backdrop);
    font-family: "Open Sans", Arial, sans-serif;
  }
  .canvas { position: relative; width: 1200px; height: 900px; }
  .card {
    position: absolute;
    top: 275px;
    width: 477px;
    height: 294px;
    overflow: hidden;
  }
  .card--front { left: 116px; background: var(--card-black-dark); }
  .card--back { left: 622px; background: var(--card-red-dark); }
  .card__sweep { position: absolute; inset: 0; width: 477px; height: 294px; }

  .wordmark {
    position: absolute;
    color: var(--ink-white);
    font-weight: 800;
    line-height: 1;
    white-space: nowrap;
  }
  .card--front .wordmark {
    left: 28px;
    top: 52px;
    font-size: 56px;
    letter-spacing: 4px;
  }
  .card--back .wordmark {
    left: 224px;
    top: 224px;
    font-size: 38px;
    letter-spacing: 3.6px;
  }
  .tagline {
    position: absolute;
    left: 225px;
    top: 262px;
    font-size: 8px;
    line-height: 1;
    letter-spacing: 2.4px;
    color: var(--tagline);
    white-space: nowrap;
  }

  .contact {
    position: absolute;
    right: 19px;
    top: 157px;
    text-align: right;
    color: var(--ink-white);
  }
  .contact__name { font-size: 17px; font-weight: 700; line-height: 22px; }
  .contact__name .surname { color: var(--accent-red); }
  .contact__role { font-size: 14px; line-height: 18px; }
  .contact__lines { margin-top: 22px; }
  .contact__line {
    display: flex;
    justify-content: flex-end;
    align-items: center;
    gap: 9px;
    font-size: 14px;
    line-height: 20px;
  }
  .contact__icon { width: 11px; height: 11px; fill: var(--accent-red); flex: none; }
</style>
</head>
<body>
<main class="canvas">

  <section class="card card--front" aria-label="Business card front">
    <svg class="card__sweep" viewBox="0 0 477 294" aria-hidden="true">
      <path d="M0 0 H477 V0 C380 120 250 270 0 294 Z" fill="var(--card-black-light)"/>
    </svg>
    <div class="wordmark">CORVALT</div>
    <div class="contact">
      <p class="contact__name">Mark <span class="surname">Pell</span></p>
      <p class="contact__role">Managing Director</p>
      <div class="contact__lines">
        <p class="contact__line">+64 027 604 91352
          <svg class="contact__icon" viewBox="0 0 24 24" aria-hidden="true"><path d="M6.6 10.8a15.1 15.1 0 0 0 6.6 6.6l2.2-2.2c.3-.3.7-.4 1-.2 1.1.4 2.3.6 3.6.6.6 0 1 .4 1 1V20c0 .6-.4 1-1 1A17 17 0 0 1 3 4c0-.6.4-1 1-1h3.5c.6 0 1 .4 1 1 0 1.3.2 2.5.6 3.6.1.3 0 .7-.2 1z"/></svg>
        </p>
        <p class="contact__line">mark.pell@corvalt-example.co.nz
          <svg class="contact__icon" viewBox="0 0 24 24" aria-hidden="true"><path d="M2 5h20v14H2z" fill="var(--accent-red)"/><path d="M3 6l9 7 9-7" fill="none" stroke="#070707" stroke-width="1.6"/></svg>
        </p>
      </div>
    </div>
  </section>

  <section class="card card--back" aria-label="Business card back">
    <svg class="card__sweep" viewBox="0 0 477 294" aria-hidden="true">
      <path d="M0 0 H477 V0 C380 120 250 270 0 294 Z" fill="var(--card-red-light)"/>
    </svg>
    <div class="wordmark">CORVALT</div>
    <p class="tagline">ALWAYS ON STANDBY</p>
  </section>

</main>
</body>
</html>
```